Quiet Harbor - Childhood Cancer Journey

In 2019, Tovin, my five-year-old, was diagnosed with stage 4 kidney cancer.

From the beginning, I said God would do his part, the doctors will do theirs, and I would do mine to save my son.

Diving into Christian beliefs and research, I learned and applied major shifts in everything we didn’t. Pulling invaluable information from fields like alternative cancer treatments coupled with Corvel Ring study, Longevity, Biohacking, Functional Medicine, and microbiome.

Tovin when from stage 4 to cancer-free in 8 months. The journey is and was very difficult, but we’ve learned and been able to help countless others.

Industry/Entity Type

Health, Wellness, Mindset, Adversity

Requirements
Nice to have
• Bright with feelings of warmth

```html
<!DOCTYPE html>
<html lang="en">
<head>
<meta charset="utf-8">
<title>Quiet Harbor — Book Cover</title>
<link rel="stylesheet" href="https://fonts.googleapis.com/css2?family=Caveat+Brush&family=Montserrat:wght@400;500&display=swap">
<style>
  :root {
    --slate: #1f2322;
    --slate-deep: #141716;
    --glow: #e9ece8;
    --basket: #8a6a43;
    --onion: #b9a57a;
    --tomato: #c9372b;
    --fig: #6e4a3c;
    --fig-green: #7d8a55;
    --apple: #c88a4a;
    --pod: #b79d7c;
    --lavender: #6f6787;
    --ink-light: #ffffff;
  }
  html, body {
    margin: 0;
    padding: 0;
    width: 800px;
    height: 1200px;
    overflow: hidden;
    background: var(--slate);
  }
  .cover {
    position: relative;
    width: 800px;
    height: 1200px;
    overflow: hidden;
    background: var(--slate);
  }
  .cover-art {
    position: absolute;
    inset: 0;
    width: 800px;
    height: 1200px;
    display: block;
  }
  .title-block {
    position: absolute;
    left: 0;
    right: 0;
    top: 820px;
    text-align: center;
    color: var(--ink-light);
  }
  .book-title {
    margin: 0;
    font-family: "Caveat Brush", cursive;
    font-weight: 400;
    font-size: 118px;
    line-height: 1;
    letter-spacing: 1px;
    text-shadow: 0 2px 10px rgba(0,0,0,0.45);
  }
  .book-tagline {
    margin: 22px auto 0;
    width: 700px;
    font-family: "Montserrat", sans-serif;
    font-weight: 500;
    font-size: 19px;
    line-height: 31px;
    text-shadow: 0 1px 6px rgba(0,0,0,0.6);
  }
  .book-author {
    position: absolute;
    left: 0;
    right: 0;
    top: 1150px;
    margin: 0;
    text-align: center;
    font-family: "Montserrat", sans-serif;
    font-weight: 400;
    font-size: 26px;
    letter-spacing: 7px;
    color: var(--ink-light);
    text-shadow: 0 1px 6px rgba(0,0,0,0.6);
  }
</style>
</head>
<body>
<main class="cover">
  <svg class="cover-art" viewBox="0 0 800 1200" role="img"
       aria-label="Overhead photo collage: a smiling father hugging his laughing young son at the centre, surrounded by a basket of garlic and potatoes, a bowl of onions, tomatoes and cucumber, a bowl of figs, apples, dried poppy pods and a lavender bundle on a dark table">
    <defs>
      <radialGradient id="family-glow" cx="50%" cy="45%" r="55%">
        <stop offset="0" stop-color="#8a6a55"/>
        <stop offset="0.45" stop-color="#b8b2a8" stop-opacity="0.85"/>
        <stop offset="0.75" stop-color="var(--glow)" stop-opacity="0.35"/>
        <stop offset="1" stop-color="var(--glow)" stop-opacity="0"/>
      </radialGradient>
      <radialGradient id="basket-tone" cx="50%" cy="40%" r="60%">
        <stop offset="0" stop-color="#c8b48e"/>
        <stop offset="1" stop-color="var(--basket)"/>
      </radialGradient>
      <radialGradient id="onion-tone" cx="40%" cy="50%" r="60%">
        <stop offset="0" stop-color="#d8ccaa"/>
        <stop offset="1" stop-color="var(--onion)" stop-opacity="0.6"/>
      </radialGradient>
      <radialGradient id="tomato-tone" cx="50%" cy="50%" r="55%">
        <stop offset="0" stop-color="var(--tomato)"/>
        <stop offset="0.7" stop-color="#8a4a3a" stop-opacity="0.7"/>
        <stop offset="1" stop-color="#6a6a55" stop-opacity="0.2"/>
      </radialGradient>
      <radialGradient id="fig-tone" cx="45%" cy="45%" r="60%">
        <stop offset="0" stop-color="var(--fig)"/>
        <stop offset="0.7" stop-color="var(--fig-green)"/>
        <stop offset="1" stop-color="#5c7a70"/>
      </radialGradient>
      <radialGradient id="apple-tone" cx="50%" cy="40%" r="60%">
        <stop offset="0" stop-color="var(--apple)"/>
        <stop offset="1" stop-color="#7a6a4a"/>
      </radialGradient>
      <linearGradient id="bottom-shade" x1="0" y1="0" x2="0" y2="1">
        <stop offset="0" stop-color="var(--slate-deep)" stop-opacity="0"/>
        <stop offset="1" stop-color="var(--slate-deep)" stop-opacity="0.75"/>
      </linearGradient>
    </defs>

    <rect class="table" width="800" height="1200" fill="var(--slate)"/>
    <rect class="basket" x="250" y="-20" width="490" height="250" rx="30" fill="url(#basket-tone)" transform="rotate(6 495 105)"/>
    <ellipse class="lavender" cx="230" cy="80" rx="40" ry="110" fill="var(--lavender)" opacity="0.7" transform="rotate(-35 230 80)"/>
    <circle class="onion-bowl" cx="50" cy="410" r="230" fill="url(#onion-tone)"/>
    <circle class="tomato-bowl" cx="720" cy="330" r="190" fill="url(#tomato-tone)"/>
    <ellipse class="family" cx="360" cy="470" rx="330" ry="340" fill="url(#family-glow)"/>
    <ellipse class="poppy-pods" cx="730" cy="820" rx="110" ry="200" fill="var(--pod)" opacity="0.55" transform="rotate(-20 730 820)"/>
    <circle class="fig-bowl" cx="120" cy="990" r="270" fill="url(#fig-tone)"/>
    <circle class="apple-bowl" cx="520" cy="1120" r="210" fill="url(#apple-tone)"/>
    <circle class="loose-tomato" cx="410" cy="800" r="38" fill="var(--tomato)"/>
    <circle class="loose-tomato" cx="370" cy="940" r="34" fill="var(--tomato)"/>
    <rect class="text-shade" y="800" width="800" height="400" fill="url(#bottom-shade)"/>
  </svg>

  <header class="title-block">
    <h1 class="book-title">Quiet Harbor</h1>
    <p class="book-tagline">A loving father, determined to guide his cancer-stricken son’s journey to a cure, discovers the Corvel Ring protocol of nourishing the body to optimum health.</p>
  </header>
  <p class="book-author">MARCUS ELLERY</p>
</main>
</body>
</html>
```